Name of company is Bluebird Meadow Shear Sharpening and Sales.Card design basic idea; I'm thinking back side just showing a sharp BLUEBIRD MEADOW. Front side: I'm thinking a tiger showing teeth and claws.With the words "Bluebird Meadow" larger type emphasized on one line.Then "Shear Sharpening and Sales" on the next line.Other info on front of card should be my name and phone #'s and address: Marcus Pellingham P (407)555-0174 CP (321)555-0138 My address is NOT to be emphasized.Can go at bottom of card. It is: 5127 Brennigan Lane Orlando FL 32899 If all that's too much to fit without looking cluttered than maybe the claw on the front with all the contact info. and just the Tiger on back of card. Whichever looks best.

Target Market(s)

Beauty Salons

Industry/Entity Type

It Company

Contact Information for Business Card

The 2 images,the claw and the tiger,could be either illustrations or photos.Whatever looks best.Got to be eye grabbing either way.

Requirements
Must have
• Contact info. Must be in color. And emphasize the identity. BLUEBIRD MEADOW.Tiger on one side.Showing TEETH. Bluebird Meadow on the other side. Showing the CLAW. .Both pics must emphasize SHARPNESS...This is a shear SHARPENING business. If one of the claw pics shows cutting grooves into something that's fine too. Card must show sharpness of the claw blade somehow.
Nice to have
• Attention grabbing. Images should jump off the card!
Should not have
• No boring cuddly tiger pics showing no teeth or claws or dull teeth or claws. No Black and whites.. No extra words other than what I've listed.

```html
<!DOCTYPE html>
<html lang="en">
<head>
<meta charset="utf-8">
<title>Bluebird Meadow Shear Sharpening – Business Cards</title>
<link href="https://fonts.googleapis.com/css2?family=Lato:wght@300;400;700;900&display=swap" rel="stylesheet">
<style>
  :root {
    --bg: #ecebe8;
    --card: #ffffff;
    --ink: #2a2a2a;
    --ink-soft: #555555;
    --accent: #f5a623;
    --art-a: #d9d9d9;
    --art-b: #9a9a9a;
  }
  * { box-sizing: border-box; margin: 0; padding: 0; }
  html, body { width: 1200px; height: 800px; overflow: hidden; }
  body {
    background: var(--bg);
    font-family: "Lato", Arial, sans-serif;
    color: var(--ink);
    position: relative;
  }
  .card {
    position: absolute;
    width: 520px;
    height: 300px;
    background: var(--card);
    border-radius: 14px;
    box-shadow: 0 10px 28px rgba(0,0,0,0.18);
    overflow: hidden;
  }
  .card--back { left: 50px; top: 110px; }
  .card--front { left: 630px; top: 110px; }

  /* logo lockup */
  .brand { display: flex; align-items: center; gap: 10px; }
  .brand__dot {
    width: 34px; height: 34px; border-radius: 50%;
    background: var(--ink); flex: none;
  }
  .brand__name {
    font-weight: 900; color: var(--accent);
    font-size: 22px; letter-spacing: 0.5px; line-height: 1;
  }
  .brand__tag {
    font-weight: 400; color: var(--ink);
    font-size: 9px; letter-spacing: 4px; margin-top: 5px;
  }

  /* back card */
  .claw-art {
    position: absolute; left: 30px; top: 45px;
    width: 290px; height: 210px; border-radius: 8px;
    background: radial-gradient(ellipse at 60% 50%, var(--art-a), var(--art-b));
  }
  .card--back .brand { position: absolute; left: 335px; top: 132px; }
  .card--back .brand__name { font-size: 14px; }
  .card--back .brand__tag { font-size: 6px; letter-spacing: 2.5px; }
  .card--back .brand__dot { width: 24px; height: 24px; }

  /* front card */
  .card--front .brand { position: absolute; left: 232px; top: 48px; }
  .rule { position: absolute; top: 118px; height: 3px; }
  .rule--dark { left: 0; width: 255px; background: var(--ink); }
  .rule--accent { left: 262px; right: 0; background: var(--accent); }

  .person { position: absolute; left: 24px; top: 64px; padding-left: 14px; }
  .person::before {
    content: ""; position: absolute; left: 0; top: 4px;
    width: 6px; height: 40px; background: var(--accent);
  }
  .person__name { font-size: 21px; font-weight: 300; color: var(--ink); line-height: 1.1; }
  .person__name b { font-weight: 900; }
  .person__role { font-size: 13px; color: var(--accent); margin-top: 2px; }

  .contacts { position: absolute; left: 28px; top: 170px; list-style: none; }
  .contacts li {
    display: flex; align-items: center; gap: 12px;
    font-size: 15px; color: var(--ink); height: 32px;
  }
  .contacts .icon {
    width: 22px; height: 22px; border-radius: 50%;
    background: var(--ink); display: flex; align-items: center; justify-content: center; flex: none;
  }
  .contacts .address { font-size: 13px; color: var(--ink-soft); }

  /* standalone lockup */
  .lockup { position: absolute; left: 55px; top: 560px; }
  .lockup .brand__dot { width: 70px; height: 70px; }
  .lockup .brand { gap: 18px; }
  .lockup .brand__name { font-size: 44px; }
  .lockup .brand__tag { font-size: 17px; letter-spacing: 7px; margin-top: 10px; }
</style>
</head>
<body>

  <section class="card card--back" aria-label="Card back">
    <div class="claw-art" role="img" aria-label="Illustration of sharp claws tearing through the card"></div>
    <div class="brand">
      <span class="brand__dot"></span>
      <div>
        <div class="brand__name">BLUEBIRD MEADOW</div>
        <div class="brand__tag">SHEAR SHARPENING</div>
      </div>
    </div>
  </section>

  <section class="card card--front" aria-label="Card front">
    <div class="brand">
      <span class="brand__dot"></span>
      <div>
        <div class="brand__name">BLUEBIRD MEADOW</div>
        <div class="brand__tag">SHEAR SHARPENING</div>
      </div>
    </div>
    <div class="rule rule--dark"></div>
    <div class="rule rule--accent"></div>

    <div class="person">
      <div class="person__name">Marcus <b>Pellingham</b></div>
      <div class="person__role">Owner</div>
    </div>

    <ul class="contacts">
      <li>
        <span class="icon">
          <svg width="12" height="12" viewBox="0 0 24 24"><path fill="#f5a623" d="M6.6 10.8a15 15 0 0 0 6.6 6.6l2.2-2.2a1 1 0 0 1 1-.25 11.4 11.4 0 0 0 3.6.57 1 1 0 0 1 1 1V20a1 1 0 0 1-1 1A17 17 0 0 1 3 4a1 1 0 0 1 1-1h3.5a1 1 0 0 1 1 1c0 1.25.2 2.45.57 3.57a1 1 0 0 1-.25 1z"/></svg>
        </span>
        (407)555-0174
      </li>
      <li>
        <span class="icon">
          <svg width="12" height="12" viewBox="0 0 24 24"><rect x="7" y="2" width="10" height="20" rx="2" fill="#f5a623"/><rect x="9" y="5" width="6" height="11" fill="#2a2a2a"/></svg>
        </span>
        (321)555-0138
      </li>
      <li>
        <span class="icon">
          <svg width="12" height="12" viewBox="0 0 24 24"><path fill="#f5a623" d="M12 2a7 7 0 0 0-7 7c0 5 7 13 7 13s7-8 7-13a7 7 0 0 0-7-7zm0 9.5A2.5 2.5 0 1 1 12 6.5a2.5 2.5 0 0 1 0 5z"/></svg>
        </span>
        <span class="address">5127 Brennigan Lane Orlando FL 32899</span>
      </li>
    </ul>
  </section>

  <div class="lockup">
    <div class="brand">
      <span class="brand__dot"></span>
      <div>
        <div class="brand__name">BLUEBIRD MEADOW</div>
        <div class="brand__tag">SHEAR SHARPENING</div>
      </div>
    </div>
  </div>

</body>
</html>
```